Hemp (cannabis) CBD Oil 3-page Blog website

The objective is 1) to look like professional/serious company, 2) to get investors excited about our Hemp business, 3) to get investor email and phone numbers and build a sense community. Potential investors should become excited that this is their “window of opportunity,” because VelLorim is made up of extraordinary people who all have made successful business before, that the location in Uruguay is a huge benefit, that we will become the biggest and best CBD-oil manufacturer in Latin America, and that we focus on all-legal medicinal CBD oil extracted from hemp.

Target Market(s)

Potential investors looking to invest between $30,000-$1,000,000 USD into a HEMP startup business, based in Uruguay, South America.

Industry/Entity Type

Business

Number of Pages Required

3 page

Font styles to use
Sans Serif

Requirements
Must have
• Three pages: Home, Members Only, News (blog).
• FOR MORE DETAIL SEE ATTACHED WORD REQUIREMENTS DOCUMENT.
Nice to have
• Uruguay colors: sky blue, golden sun. Medicinal. Legal. Mainstream. Hemp. Professional people. Opportunity/Money/Investor. Uruguay. Latin America. 1st to Market.
Should not have
• Marijuana (HEMP yes, marijuana NO), anything that looks illegal.

```html
<!DOCTYPE html>
<html lang="en">
<head>
<meta charset="utf-8">
<title>VelLorim – Hemp CBD Oil, Uruguay</title>
<link href="https://fonts.googleapis.com/css2?family=Roboto:wght@300;400;500;700&display=swap" rel="stylesheet">
<style>
:root{
  --green:#3fae49;
  --green-dark:#2c8a37;
  --blue:#1f7fc4;
  --sky:#2aa5e0;
  --orange:#f39419;
  --ink:#333;
  --muted:#777;
  --light:#f1f1f1;
  --line:#ddd;
  --white:#fff;
}
*{box-sizing:border-box;margin:0;padding:0}
html,body{width:1200px;height:2896px;overflow:hidden}
body{font-family:'Roboto',sans-serif;color:var(--ink);background:var(--white);position:relative}
.btn{display:inline-block;border:0;color:#fff;font:500 12px 'Roboto',sans-serif;text-transform:uppercase;padding:12px 22px;letter-spacing:.5px}
.btn-blue{background:var(--blue)}
.btn-orange{background:var(--orange)}
.btn-green{background:var(--green)}

/* header */
.site-header{position:absolute;top:0;left:0;width:1200px;height:100px;background:var(--white);display:flex;align-items:center;padding:0 40px;z-index:2}
.brand{display:flex;align-items:center;gap:10px;font:700 28px 'Roboto',sans-serif;color:var(--green)}
.brand-dot{width:14px;height:14px;border-radius:50%;background:var(--sky)}
.main-nav{margin-left:auto;display:flex;gap:26px;font-size:13px;color:#555}
.head-actions{display:flex;gap:8px;margin-left:30px}
.head-actions .btn{padding:7px 12px;font-size:10px}

/* hero */
.hero{position:absolute;top:100px;left:0;width:1200px;height:400px;background:linear-gradient(180deg,#d9e6d2 0%,#9fc48a 35%,#5d8e45 70%,#3c6a2d 100%)}
.hero-panel{position:absolute;left:672px;top:60px;width:380px;height:270px;background:rgba(20,30,25,.72);padding:26px 28px;color:#fff}
.hero-panel h1{font-size:42px;font-weight:700;margin-bottom:12px}
.hero-panel p{font-size:13px;line-height:1.5;color:#e6e6e6;margin-bottom:24px}
.hero-panel .btn{margin-right:10px}

/* blog */
.latest-blog{position:absolute;top:500px;left:0;width:1200px;height:345px;background:var(--light);padding:28px 120px}
.section-title{font-size:34px;font-weight:400;color:#444}
.blog-arrows{position:absolute;right:120px;top:40px;font-size:18px;color:#999;letter-spacing:10px}
.posts{display:flex;gap:60px;margin-top:26px}
.post{display:flex;gap:24px;width:460px}
.post-thumb{flex:none;width:150px;height:150px;border-radius:50%;background:radial-gradient(circle at 40% 40%,#a5c98c,#557f3f)}
.post h3{font-size:17px;font-weight:500;margin-bottom:8px}
.post-date{display:inline-block;background:var(--blue);color:#fff;font-size:11px;padding:5px 12px;margin-bottom:10px}
.post p{font-size:12px;line-height:1.5;color:var(--muted)}
.read-more{display:block;margin-top:14px;font-size:11px;font-weight:500;color:#444}

/* about */
.about{position:absolute;top:845px;left:0;width:1200px;height:575px;text-align:center;padding-top:40px}
.about h2{font-size:40px;font-weight:400;color:#555}
.about h2 b{font-weight:700;color:#333}
.about-lead{width:860px;margin:14px auto 0;font-size:12px;line-height:1.6;color:var(--muted)}
.about-lead a{color:var(--blue);font-weight:500}
.cbd-cycle{position:absolute;left:150px;top:160px}
.about-photo{position:absolute;left:612px;top:210px;width:430px;height:320px;background:linear-gradient(180deg,#b9cf8c,#7fa44f 55%,#4f7432)}

/* investor band */
.investor-band{position:absolute;top:1420px;left:0;width:1200px;height:300px;background:#e7e7e7}
.band-photo{position:absolute;left:0;top:0;width:620px;height:300px;background:linear-gradient(100deg,#6fb6d6,#a9d7e6 45%,#7fb58a 100%)}
.band-copy{position:absolute;left:648px;top:80px;width:420px}
.band-copy p{font-size:17px;color:var(--blue);line-height:1.35;margin-bottom:18px}
.field{display:block;width:420px;height:40px;background:#fff;border:1px solid var(--line);font-size:13px;color:#999;padding:12px 14px;margin-bottom:14px}
.band-copy .btn{width:200px;text-align:center;margin-right:16px}
.band-copy .btn:last-child{margin-right:0}

/* team */
.team{position:absolute;top:1720px;left:0;width:1200px;height:820px}
.team-intro{position:absolute;left:110px;top:90px;width:210px;font-size:17px;line-height:1.35;text-transform:uppercase;color:var(--green)}
.team-intro .eyebrow{color:var(--blue);font-size:16px}
.team-intro strong{display:block;font-size:26px;color:var(--blue);font-weight:700;margin-bottom:14px}
.leaf-art{position:absolute;left:120px;top:560px;width:190px;height:190px;border-radius:50% 10% 50% 10%;background:radial-gradient(circle,#5f9a3d,#2f6a22)}
.team-grid{position:absolute;left:352px;top:92px;display:grid;grid-template-columns:repeat(3,228px);gap:44px 80px}
.member{width:228px;height:320px;border:1px solid var(--line);background:#fff;position:relative;overflow:hidden}
.member-photo{height:226px;background:linear-gradient(180deg,#d8d8d8,#a9a9a9)}
.member h4{font-size:15px;font-weight:500;text-align:center;margin-top:14px}
.member p{font-size:11px;text-align:center;color:var(--muted);line-height:1.4;margin-top:5px}
.member::after{content:"";position:absolute;right:0;bottom:0;border-left:34px solid transparent;border-bottom:34px solid var(--green)}

/* contact */
.contact{position:absolute;top:2540px;left:0;width:1200px;height:310px;background:var(--light)}
.map-art{position:absolute;left:110px;top:26px;width:250px;height:270px;border-radius:50% 50% 8px 8px;background:linear-gradient(180deg,#fff 0 18%,#d6e9c2 18%,#9cc97a 100%)}
.map-label{position:absolute;left:250px;top:40px;font-size:12px;color:#555;width:100px;text-align:center}
.map-country{position:absolute;left:210px;top:260px;font-size:12px;color:#555;font-weight:500;letter-spacing:1px}
.contact h3{font-size:28px;font-weight:400;color:#444;margin-bottom:16px}
.details{position:absolute;left:470px;top:30px;width:280px}
.details li{list-style:none;display:flex;gap:10px;font-size:12px;color:#555;line-height:1.45;margin-bottom:14px}
.details svg{flex:none}
.inquiry{position:absolute;left:800px;top:30px;width:290px}
.inquiry .field{width:290px;height:32px;font-size:12px;padding:8px 12px;margin-bottom:8px}
.inquiry .msg{height:60px}
.inquiry .btn{padding:8px 18px;font-size:10px;background:var(--blue)}

.site-footer{position:absolute;top:2850px;left:0;width:1200px;height:46px;background:var(--green);color:#e8f5e8;font-size:12px;text-align:center;line-height:46px}
</style>
</head>
<body>

<header class="site-header">
  <div class="brand"><span class="brand-dot"></span>VelLorim</div>
  <nav class="main-nav"><span>Home</span><span>Members Only</span><span>About</span><span>Team</span><span>News Blog</span><span>Contact</span></nav>
  <div class="head-actions"><span class="btn btn-blue">Members</span><span class="btn btn-green">Get Password</span></div>
</header>

<section class="hero" role="img" aria-label="Hemp plants growing in rows inside a bright greenhouse">
  <div class="hero-panel">
    <h1>VelLorim</h1>
    <p>Lorem ipsum dolor sit amet, consectetur adipiscing elit, sed diam nonummy nibh euismod tincidunt ut laoreet dolore magna aliquam erat volutpat.</p>
    <span class="btn btn-blue">Become a Member</span><span class="btn btn-orange">Members Only</span>
  </div>
</section>

<section class="latest-blog">
  <h2 class="section-title">Latest Blog</h2>
  <div class="blog-arrows">‹ ›</div>
  <div class="posts">
    <article class="post">
      <div class="post-thumb" role="img" aria-label="Close view of hemp leaves"></div>
      <div>
        <h3>Diam Nonummy Nibhal Lorem ipsum</h3>
        <span class="post-date">Jan 14, 2017</span>
        <p>Uruguay-based hemp growers report steady progress on licensed medicinal crops this season. Field teams expect the first harvest to be processed ahead of plan, with lab testing now underway.</p>
        <span class="read-more">Read More »</span>
      </div>
    </article>
    <article class="post">
      <div class="post-thumb" role="img" aria-label="Young hemp plants in the field"></div>
      <div>
        <h3>Diam Nonummy Nibhal Lorem ipsum</h3>
        <span class="post-date">Jan 14, 2017</span>
        <p>Uruguay-based hemp growers report steady progress on licensed medicinal crops this season. Field teams expect the first harvest to be processed ahead of plan, with lab testing now underway.</p>
        <span class="read-more">Read More »</span>
      </div>
    </article>
  </div>
</section>

<section class="about">
  <h2>About to <b>VelLorim</b></h2>
  <p class="about-lead">VelLorim is a manufacturing startup company in Uruguay, South America. It will grow a specially engineered strain of high CBD hemp, extract and refine the valuable plant oils, and package them into therapeutic products. The products will be sold to customers where new markets open due to recognition of cannabis therapy and local laws, and in larger specific demand wherever hemp oil is lawfully sold. <a>Read More</a></p>
  <svg class="cbd-cycle" width="400" height="400" viewBox="0 0 400 400" aria-label="Cycle of CBD production steps">
    <g fill="none" stroke-width="70" transform="rotate(-90 200 200)">
      <circle cx="200" cy="200" r="120" stroke="#1fa3a0" stroke-dasharray="120 634"/>
      <circle cx="200" cy="200" r="120" stroke="#2a7fc5" stroke-dasharray="120 634" stroke-dashoffset="-126"/>
      <circle cx="200" cy="200" r="120" stroke="#5fb740" stroke-dasharray="120 634" stroke-dashoffset="-252"/>
      <circle cx="200" cy="200" r="120" stroke="#f28b1e" stroke-dasharray="120 634" stroke-dashoffset="-378"/>
      <circle cx="200" cy="200" r="120" stroke="#e0427a" stroke-dasharray="120 634" stroke-dashoffset="-504"/>
      <circle cx="200" cy="200" r="120" stroke="#555c66" stroke-dasharray="120 634" stroke-dashoffset="-630"/>
    </g>
    <circle cx="200" cy="200" r="72" fill="#d7d7d7"/>
    <text x="200" y="214" text-anchor="middle" font-family="Roboto,sans-serif" font-size="40" font-weight="700" fill="#fff">CBD</text>
    <g font-family="Roboto,sans-serif" font-size="10" fill="#fff" text-anchor="middle">
      <text x="255" y="98">Seed Cultivation</text>
      <text x="318" y="195">Gene Selection</text>
      <text x="265" y="310">Extraction</text>
      <text x="145" y="310">Oil Refinement</text>
      <text x="84" y="205">Health Products</text>
      <text x="140" y="98">Distribution</text>
    </g>
  </svg>
  <div class="about-photo" role="img" aria-label="Farmer inspecting tall hemp crop in an open field"></div>
</section>

<section class="investor-band">
  <div class="band-photo" role="img" aria-label="Gloved hand handling seedlings in a laboratory"></div>
  <div class="band-copy">
    <p>VelLorim is not just designing CBD products, it is designed to maximize investor returns.</p>
    <span class="field">Password</span>
    <span class="btn btn-green">Members Only</span><span class="btn btn-blue">Get Password</span>
  </div>
</section>

<section class="team">
  <div class="team-intro">
    <span class="eyebrow">Our</span>
    <strong>Team</strong>
    Our team is composed of experts, each an authority in their fields<br><br>and each of us has a successful record of starting business.
  </div>
  <div class="leaf-art" role="img" aria-label="Green hemp leaf decoration"></div>
  <div class="team-grid">
    <div class="member"><div class="member-photo" role="img" aria-label="Portrait of team member"></div><h4>Dra. Selma Ruvel</h4><p>Regulatory Affairs, Import/Export<br>Management, Medical Director</p></div>
    <div class="member"><div class="member-photo" role="img" aria-label="Portrait of team member"></div><h4>Tomas Brenwick</h4><p>Business Development, Quality<br>Assurance, Operations Management</p></div>
    <div class="member"><div class="member-photo" role="img" aria-label="Portrait of team member"></div><h4>Elio Marsant</h4><p>Business Development,<br>Strategic Planning</p></div>
    <div class="member"><div class="member-photo" role="img" aria-label="Portrait of team member"></div><h4>Dario Lenz</h4><p>Plant Genetic Specialist,<br>Agronomy Director</p></div>
    <div class="member"><div class="member-photo" role="img" aria-label="Portrait of team member"></div><h4>Matias Orvell</h4><p>Marketing &amp; Finance Director,<br>Risk Management, IT</p></div>
    <div class="member"><div class="member-photo" role="img" aria-label="Portrait of team member"></div><h4>Nico Caldren</h4><p>Business Manager,<br>Investor Relations</p></div>
  </div>
</section>

<section class="contact">
  <div class="map-art" role="img" aria-label="Map of South America with Uruguay highlighted"></div>
  <div class="map-label">Map of<br>South America</div>
  <div class="map-country">URUGUAY</div>
  <div class="details">
    <h3>Contact Details</h3>
    <ul>
      <li><svg width="14" height="16" viewBox="0 0 14 16"><path d="M7 0a5 5 0 0 0-5 5c0 4 5 11 5 11s5-7 5-11a5 5 0 0 0-5-5zm0 7a2 2 0 1 1 0-4 2 2 0 0 1 0 4z" fill="#1f7fc4"/></svg><span><b>VelLorim</b><br>1180 Calle Rivera, Oficina 4<br>Montevideo 11300, Uruguay</span></li>
      <li><svg width="14" height="14" viewBox="0 0 14 14"><path d="M3 0l3 3-2 2c1 2 3 4 5 5l2-2 3 3-2 3C6 14 0 8 0 2z" fill="#1f7fc4"/></svg><span>+598 2400 1177</span></li>
      <li><svg width="14" height="12" viewBox="0 0 14 12"><rect width="14" height="12" fill="#1f7fc4"/><path d="M0 0l7 6 7-6" stroke="#fff" fill="none"/></svg><span>info@vellorim.com</span></li>
    </ul>
  </div>
  <div class="inquiry">
    <h3>Quick Inquiry</h3>
    <span class="field">Name</span>
    <span class="field">Email</span>
    <span class="field msg">Message</span>
    <span class="btn">Submit</span>
  </div>
</section>

<footer class="site-footer">Copyright © 2017 VelLorim. All Rights Reserved.</footer>

</body>
</html>
```